Grain Clear Kitchen Web Design

We are looking for designs for a homepage for a gluten free, health food website.

We are looking for the site to be a shop, as well as a resource/information source for users. We will also look to incorporate recipes, blogs, forums and potentially some other useful information.

We want to ensure that the website is user-friendly, does not have a corporate feel, but is still classy.

We want to have high quality photographic images in the background, with text in the foreground - but these things will need to compliment each other well. e.g recipe of the week integrated onto the background photo and the 'shop' in the foreground.

We have seen a site that we quite like and although we like the design, we do not want to completely emulate this. However, it is a useful starting point for designers and perhaps some inspiration www.brightpantryhall.example

We already have a logo - see attached - which will need to be fully integrated into the design.

We do want a colourful design, but mainly in terms of the images rather than the graphics.
Updates

Please note:

We are pleased with the designs to date, for the most part. We would like you all to note, however, that we are much preferring the lighter designs - ones that make the sites feel brighter - rather than those which are darker in appearance.

We would also like to see less space allocated to the main image, within the context of the site as a whole.

Thanks.

We have eliminated those which we feel are not what we are looking for. We are still keen to see some more designs and are still looking for something unique. There are some good things in all of the designs that we have not eliminated, however we still feel there is room for more inspiration.

Thanks.

Target Market(s)

Our audience are body conscience people looking for health food products. They are also those who are potentially looking for a new lifestyle/life cha

Industry/Entity Type

Health

Requirements
Must have
• Our logo - attached, can provide variations in due course.

Navigational features as per mock up attached.

Social network integration.

NB: we only need one (home) page for this.

```html
<!DOCTYPE html>
<html lang="en">
<head>
<meta charset="utf-8">
<title>Grain Clear Kitchen – Home</title>
<link href="https://fonts.googleapis.com/css2?family=Lobster&family=Open+Sans:wght@400;600;700&display=swap" rel="stylesheet">
<style>
:root{
  --ink:#2a2321;
  --ink-soft:#3a302c;
  --red:#b3262b;
  --red-dark:#8e1c20;
  --tan:#d9b68a;
  --tan-light:#efdcc0;
  --brown:#a9764a;
  --cream:#fbf7f1;
  --white:#ffffff;
  --grey:#6d6561;
}
*{box-sizing:border-box;margin:0;padding:0}
html,body{width:1200px;height:2900px;overflow:hidden;background:var(--white)}
body{font-family:"Open Sans",Arial,sans-serif;color:var(--ink)}
.page{position:relative;width:1200px;height:2900px;overflow:hidden;background:var(--white)}
.abs{position:absolute}
.script{font-family:"Lobster",cursive;font-weight:400}

/* hero */
.hero{left:0;top:0;width:1200px;height:600px;
  background:linear-gradient(160deg,#6b4a33 0%,#b98a5a 30%,#e8c79a 55%,#d9913f 75%,#8a4a22 100%)}
.hero-photo-plate{left:420px;top:330px;width:760px;height:300px;border-radius:50%;
  background:radial-gradient(ellipse at center,#f3d27a 0%,#e0a84a 45%,#c9602e 75%,rgba(255,255,255,0) 100%)}
.top-bar{right:0;top:0;width:360px;height:100px;background:var(--ink);border-bottom-left-radius:60px;
  color:var(--white);font-size:15px;font-weight:600}
.top-bar .search{position:absolute;left:120px;top:18px;display:flex;align-items:center;gap:10px}
.top-bar .search-box{width:150px;height:22px;background:var(--white);border-radius:3px}
.top-bar .top-links{position:absolute;left:110px;top:58px;display:flex;gap:22px}
.top-bar .top-links .active{color:var(--tan)}
.brand{left:0;top:0;width:160px;height:160px;background:var(--ink);border-bottom-right-radius:80px;
  display:flex;align-items:center;justify-content:center;text-align:center;
  color:var(--white);font-size:20px;font-weight:700;line-height:1.2;padding:0 18px}
.main-nav{left:0;top:160px;width:140px;height:380px;background:var(--ink-soft);padding-top:8px}
.main-nav li{list-style:none;color:var(--white);font-size:15px;font-weight:600;height:42px;line-height:42px;padding-left:18px}
.main-nav li.current{background:var(--red)}
.sub-nav{left:140px;top:362px;width:160px;height:180px;background:rgba(42,35,33,.92);padding-top:10px}
.sub-nav li{list-style:none;color:var(--white);font-size:14px;font-weight:600;height:38px;line-height:38px;padding-left:20px}
.sub-nav li.current{color:var(--tan)}
.hero-title{left:240px;top:300px;font-size:88px;color:var(--white);text-shadow:0 3px 10px rgba(0,0,0,.45)}
.hero-cta{left:480px;top:400px;font-size:50px;color:var(--white);font-family:"Open Sans",Arial,sans-serif;font-weight:400;text-shadow:0 2px 8px rgba(0,0,0,.4)}

/* recipe of the week */
.recipe-week{left:0;top:600px;width:1200px;height:470px;
  background:linear-gradient(180deg,var(--tan) 0%,var(--tan-light) 35%,#f6ead8 100%)}
.recipe-week-title{left:170px;top:640px;font-size:56px;color:var(--white);text-shadow:0 2px 4px rgba(0,0,0,.25)}
.recipe-week-title span{color:var(--red)}
.cupcake{left:140px;top:720px;width:300px;height:300px;border-radius:50%;
  background:radial-gradient(circle at 50% 40%,#fff7f3 0%,#f6d3cb 45%,#d98a72 80%,#c46a53 100%)}
.products-used{left:520px;top:730px;font-size:14px;line-height:21px;color:var(--red)}
.products-used .label{color:var(--white);font-style:italic;font-weight:600;margin-bottom:4px}
.bon-appetit{left:920px;top:620px;width:170px;height:170px;border-radius:50%;border:3px solid var(--ink);
  display:flex;align-items:center;justify-content:center;text-align:center;font-size:36px;line-height:1.1;color:var(--ink)}
.recipe-text{left:520px;top:860px;width:600px;font-size:13px;line-height:19px;color:var(--grey)}
.recipe-text p{margin-bottom:10px}
.recipe-text .more{color:var(--red);font-weight:700}

/* products */
.products{left:0;top:1070px;width:1200px;height:430px;
  background:linear-gradient(135deg,#3d6b2c 0%,#b32a1e 30%,#d9432b 55%,#f0b47a 78%,#5b8a36 100%)}
.products-title{left:520px;top:1155px;font-size:50px;color:var(--white);text-shadow:0 2px 8px rgba(0,0,0,.45)}
.product-card{top:1225px;width:230px;height:200px;background:var(--white);box-shadow:0 4px 12px rgba(0,0,0,.3)}
.product-card.featured{background:var(--red)}
.product-card .name{position:absolute;top:14px;left:0;width:100%;text-align:center;color:var(--white);font-weight:700;font-size:18px}
.price{position:absolute;left:85px;top:52px;width:60px;height:60px;border-radius:50%;background:var(--red-dark);
  border:3px solid var(--white);color:var(--white);font-size:15px;font-weight:700;display:flex;align-items:center;justify-content:center}
.product-card .recipe-link{position:absolute;left:0;top:128px;width:100%;background:var(--ink);color:var(--white);font-size:12px;text-align:center;padding:6px 0;font-style:italic}
.product-card .bag{position:absolute;left:0;bottom:10px;width:100%;text-align:center;color:var(--white);font-size:14px;font-weight:600}
.product-photo{position:absolute;left:14px;top:14px;width:202px;height:172px}
.share-row{top:1432px;width:230px;height:26px;display:flex;gap:8px;justify-content:center}
.share-row i{display:block;width:22px;height:22px;border-radius:50%;background:var(--white)}

/* blog & forum */
.strip-white{left:0;width:1200px;background:var(--white)}
.letter-mark{width:220px;height:220px;border-radius:40% 55% 45% 50%;background:linear-gradient(160deg,#e9c8a0,#c8915e)}
.post{width:220px;font-size:12px;line-height:17px;color:var(--grey)}
.post h3{font-size:12px;font-weight:700;color:var(--red);margin-bottom:4px}
.post .read{color:var(--red);font-weight:700;margin-top:6px;display:block}
.view-more{width:100px;height:100px;border-radius:50%;background:var(--red-dark);color:var(--white);
  font-size:22px;line-height:1.05;display:flex;align-items:center;justify-content:center;text-align:center}
.pasta-band{left:0;top:1820px;width:1200px;height:100px;
  background:linear-gradient(90deg,#4e7d2e 0%,#e4b867 25%,#f1d48e 55%,#c9742f 80%,#5a8a33 100%)}

/* popular recipes */
.popular{left:0;top:2180px;width:1200px;height:470px;
  background:linear-gradient(160deg,#d9a65a 0%,#f0d49a 35%,#c76a2e 70%,#4f7a2f 100%)}
.popular-title{left:130px;top:2240px;font-size:50px;color:var(--white);text-shadow:0 2px 8px rgba(0,0,0,.45)}
.recipe-circle{width:280px;height:280px;border-radius:50%;border:6px solid var(--white);box-shadow:0 4px 12px rgba(0,0,0,.3)}
.recipe-circle.feature{background:var(--tan-light);display:flex;flex-direction:column;align-items:center;justify-content:center;text-align:center}
.recipe-circle.feature .script{font-size:36px;color:var(--red)}
.recipe-circle.feature .note{font-size:15px;color:var(--grey);margin-top:8px;line-height:1.4}

/* footer */
.footer{left:0;top:2650px;width:1200px;height:250px;background:var(--ink);color:var(--white)}
.footer ul{position:absolute;top:30px;list-style:none;font-size:14px;font-weight:600;line-height:34px}
.footer .social{position:absolute;left:800px;top:80px;display:flex;gap:14px}
.footer .social i{display:block;width:26px;height:26px;border-radius:50%;background:var(--white)}
.footer .copy{position:absolute;left:800px;top:130px;font-size:11px;color:#b9b0aa;line-height:17px}
</style>
</head>
<body>
<div class="page">

  <!-- hero -->
  <div class="abs hero" role="img" aria-label="Photograph of a plate of Mediterranean pasta with tomato sauce on a kitchen table"></div>
  <div class="abs hero-photo-plate" role="img" aria-label="Close view of pasta with sauce and a fork"></div>

  <div class="abs top-bar">
    <div class="search">search <span class="search-box"></span></div>
    <div class="top-links"><span class="active">HOME</span><span>LOG IN</span><span>CONTACT US</span></div>
  </div>

  <div class="abs brand">Grain Clear Kitchen</div>
  <ul class="abs main-nav">
    <li>SHOP</li>
    <li>OUR STORY</li>
    <li>BLOG</li>
    <li>HINTS &amp; TIPS</li>
    <li class="current">RECIPES</li>
    <li>FORUMS</li>
  </ul>
  <ul class="abs sub-nav">
    <li>MEALS</li>
    <li class="current">DESSERTS</li>
    <li>FOR KIDS</li>
    <li>LOW CALORY</li>
  </ul>

  <div class="abs hero-title script">Mediterranean Pasta</div>
  <div class="abs hero-cta">make this recipe &gt;&gt;</div>

  <!-- recipe of the week -->
  <div class="abs recipe-week"></div>
  <div class="abs recipe-week-title script">Recipe of the week: <span>Cupcakes</span></div>
  <div class="abs cupcake" role="img" aria-label="Photograph of a cupcake with white frosting and red sugar hearts"></div>
  <div class="abs products-used">
    <div class="label">products used:</div>
    <div>Rice flour blend</div>
    <div>Organic cane sugar</div>
    <div>Free range eggs</div>
    <div>Vanilla extract</div>
    <div>Sugar hearts</div>
  </div>
  <div class="abs bon-appetit script">bon<br>appetit</div>
  <div class="abs recipe-text">
    <p>Soft, light and fully gluten free, these little cakes are a favourite at every party. We mix a blend of rice and almond flour with fresh eggs, butter and a touch of vanilla, then bake them until golden and springy. Top each one with a swirl of cream frosting and a few red sugar hearts for a treat that looks as good as it tastes.</p>
    <p>Preheat the oven, line a tray with paper cases and whisk the butter and sugar until pale. Beat in the eggs one by one, fold in the flour and milk, then fill each case two thirds full. Bake for eighteen minutes, cool fully on a rack and decorate just before serving. <span class="more">read more &gt;&gt;</span></p>
  </div>

  <!-- products -->
  <div class="abs products" role="img" aria-label="Photograph of fresh red tomatoes on the vine with green leaves"></div>
  <div class="abs products-title script">Popular Gluten-Free Products</div>

  <div class="abs product-card featured" style="left:200px">
    <div class="name">Product Name</div>
    <div class="price">$9.99</div>
    <div class="recipe-link">recipes using this product &gt;&gt;</div>
    <div class="bag">send to bag</div>
  </div>
  <div class="abs share-row" style="left:200px"><i></i><i></i><i></i><i></i><i></i><i></i></div>

  <div class="abs product-card" style="left:470px">
    <div class="product-photo" role="img" aria-label="Product photo of a glass jar of gluten free spread" style="background:linear-gradient(180deg,#e9dfb0,#c9a85a)"></div>
  </div>
  <div class="abs share-row" style="left:470px"><i></i><i></i><i></i><i></i><i></i><i></i></div>

  <div class="abs product-card" style="left:740px">
    <div class="product-photo" role="img" aria-label="Product photo of a box of gluten free breadsticks" style="background:linear-gradient(180deg,#f2e6c8,#d8b070)"></div>
  </div>
  <div class="abs share-row" style="left:740px"><i></i><i></i><i></i><i></i><i></i><i></i></div>

  <!-- blog -->
  <div class="abs strip-white" style="top:1500px;height:320px"></div>
  <div class="abs letter-mark" style="left:130px;top:1550px" role="img" aria-label="Decorative brown blog emblem"></div>
  <div class="abs post" style="left:380px;top:1570px">
    <h3>BLOG TITLE</h3>
    Our favourite tips for baking bread at home without wheat, plus a simple starter you can keep going all year round in your own kitchen.
    <span class="read">read more &gt;&gt;</span>
  </div>
  <div class="abs post" style="left:620px;top:1570px">
    <h3>BLOG TITLE</h3>
    How to read food labels and spot hidden gluten in sauces, soups and snacks so that every trip to the shop feels calm and easy.
    <span class="read">read more &gt;&gt;</span>
  </div>
  <div class="abs post" style="left:860px;top:1570px">
    <h3>BLOG TITLE</h3>
    A week of quick family dinners that are bright, fresh and free from grains, with a handy shopping list to print and take along.
    <span class="read">read more &gt;&gt;</span>
  </div>
  <div class="abs view-more script" style="left:1040px;top:1710px">view<br>more</div>

  <div class="abs pasta-band" role="img" aria-label="Photograph of dry pasta with basil leaves"></div>

  <!-- forum -->
  <div class="abs strip-white" style="top:1920px;height:260px"></div>
  <div class="abs letter-mark" style="left:130px;top:1940px" role="img" aria-label="Decorative brown forum emblem"></div>
  <div class="abs post" style="left:380px;top:1960px">
    <h3>FORUM TITLE</h3>
    Members share their best swaps for pizza bases and ask which flours hold together best when baked thin and crisp.
    <span class="read">read more &gt;&gt;</span>
  </div>
  <div class="abs post" style="left:620px;top:1960px">
    <h3>FORUM TITLE</h3>
    Eating out safely: a friendly thread on which questions to ask in cafes and restaurants before ordering a meal.
    <span class="read">read more &gt;&gt;</span>
  </div>
  <div class="abs post" style="left:860px;top:1960px">
    <h3>FORUM TITLE</h3>
    New to the lifestyle? Say hello, tell us your story and pick up advice from people who have been there before.
    <span class="read">read more &gt;&gt;</span>
  </div>
  <div class="abs view-more script" style="left:1040px;top:2070px">view<br>more</div>

  <!-- popular recipes -->
  <div class="abs popular" role="img" aria-label="Photograph of pasta and fresh herbs on a kitchen table"></div>
  <div class="abs popular-title script">Most Popular Recipies</div>
  <div class="abs recipe-circle feature" style="left:160px;top:2320px">
    <div class="script">Birthday Cake</div>
    <div class="note">view photo, recipe<br>and video &gt;&gt;</div>
  </div>
  <div class="abs recipe-circle" style="left:480px;top:2320px;background:radial-gradient(circle,#f3efe6 0%,#c9b48a 55%,#6e8a4a 100%)" role="img" aria-label="Photograph of a plated salad dish"></div>
  <div class="abs recipe-circle" style="left:790px;top:2320px;background:radial-gradient(circle,#f6f1e8 0%,#8a5a3a 50%,#3a2a22 100%)" role="img" aria-label="Photograph of chocolate dessert squares on a plate"></div>

  <!-- footer -->
  <footer class="abs footer">
    <ul style="left:150px"><li>HOME</li><li>SITE MAP</li><li>FAQS</li><li>CONTACT US</li><li>PRIVACY POLICY</li></ul>
    <ul style="left:370px"><li>SHOP</li><li>OUR STORY</li><li>HINTS &amp; TIPS</li><li>RECIPES</li></ul>
    <ul style="left:600px"><li>BLOG</li><li>FORUMS</li></ul>
    <div class="social"><i></i><i></i><i></i><i></i><i></i><i></i></div>
    <div class="copy">Copyright © 2013 Grain Clear Kitchen<br>All Rights Reserved<br>Terms of Use</div>
  </footer>

</div>
</body>
</html>
```